Banner Ad Design Project

We are a SEO company and need a banner design for our new service, the highlights being:

- Pay Per Performance SEO service
- Guaranteed Zumbly page 1 ranking
- Only $197 per month (+ performance bonus)

Can be all on one static banner or made into an animated GIF - designers choice...

Site URL (not up yet) will be RankNest412.com (by velHelm) - this is a spinoff site of our existing business, velHelm LLC - logo attached and should be included on the banner.

Industry/Entity Type

Business

Requirements
Must have
• Banner delivered in multiple sizes:
- 200 x 200
- 250 x 250
- 300 x 250
- 336 x 280
- 468 x 60
- 728 x 90
- 120 x 600
- 160 x 600

```html
<!DOCTYPE html>
<html lang="en">
<head>
<meta charset="utf-8">
<title>velHelm – Innovative Web Solutions banner set</title>
<link rel="stylesheet" href="https://fonts.googleapis.com/css2?family=Electrolize&family=Didact+Gothic&display=swap">
<style>
  :root{
    --backdrop:#1d1d1f;
    --navy:#263a5e;
    --navy-deep:#1f3050;
    --orange:#f28c1e;
    --green:#84c12e;
    --green-dark:#4d931a;
    --white:#ffffff;
    --paper:#f1f1f1;
    --logo-blue:#1f3f8f;
    --text-light:#f4f6fa;
  }
  *{box-sizing:border-box;margin:0;padding:0}
  html,body{width:1200px;height:899px;overflow:hidden;background:var(--backdrop)}
  .stage{position:absolute;left:0;top:0;width:1126px;height:844px;transform:scale(1.0657);transform-origin:0 0}

  .banner{position:absolute;overflow:hidden;background:var(--navy);box-shadow:0 0 0 2px #d9d9d9;font-family:"Didact Gothic",sans-serif;color:var(--text-light)}
  .headline{position:absolute;font-family:"Electrolize",sans-serif;color:var(--orange);font-weight:400;white-space:nowrap}
  .features{position:absolute;list-style:none}
  .features li{position:relative;padding-left:18px}
  .features li svg{position:absolute;left:0;top:3px;width:12px;height:10px}
  .cta{position:absolute;display:flex;align-items:center;justify-content:center;border-radius:3px;
       background:linear-gradient(#93cd3c,var(--green-dark));color:var(--white);
       font-family:"Electrolize",sans-serif;box-shadow:0 1px 2px rgba(0,0,0,.35)}
  .brand{position:absolute;display:flex;align-items:center}
  .brand-dot{border-radius:50%;background:var(--green);flex:none}
  .brand-name{font-family:"Electrolize",sans-serif;color:var(--logo-blue);white-space:nowrap}
  .photo{position:absolute;background:linear-gradient(160deg,rgba(38,58,94,0) 0%,#6b5447 35%,#c9c3c0 70%,#eeeeee 100%);border-radius:40% 40% 0 0}

  /* 160 x 600 skyscraper */
  .skyscraper{left:137px;top:175px;width:159px;height:600px}
  .skyscraper .top{position:absolute;left:0;top:0}
  .skyscraper .brand{left:0;top:6px;width:159px;flex-direction:column;gap:10px}
  .skyscraper .brand-dot{width:66px;height:66px}
  .skyscraper .brand-name{font-size:34px}
  .skyscraper .headline{left:0;width:169px;top:164px;text-align:center;font-size:23px;line-height:27px;white-space:normal}
  .skyscraper .features{left:8px;top:266px;font-size:12.5px;line-height:17px}
  .skyscraper .features li{margin-bottom:8px}
  .skyscraper .photo{left:30px;top:398px;width:108px;height:134px}
  .skyscraper .footer{position:absolute;left:0;top:532px;width:159px;height:68px;background:linear-gradient(var(--white),var(--paper));border-top:3px solid var(--green)}
  .skyscraper .cta{left:10px;top:16px;width:138px;height:35px;font-size:19px}

  /* 728 x 90 leaderboard */
  .leaderboard{left:335px;top:174px;width:728px;height:90px}
  .leaderboard .top{position:absolute;left:0;top:0}
  .leaderboard .brand{left:22px;top:4px;width:130px;flex-direction:column;gap:4px}
  .leaderboard .brand-dot{width:40px;height:40px}
  .leaderboard .brand-name{font-size:27px;line-height:30px}
  .leaderboard .headline{left:206px;top:6px;font-size:24px}
  .leaderboard .features{top:43px;font-size:10px;line-height:13px}
  .leaderboard .features li{padding-left:17px;margin-bottom:10px}
  .leaderboard .features li svg{width:10px;height:8px;top:3px}
  .leaderboard .col-a{left:191px}
  .leaderboard .col-b{left:392px}
  .leaderboard .photo{left:527px;top:2px;width:66px;height:88px}
  .leaderboard .cta{left:602px;top:33px;width:118px;height:32px;font-size:18px}

  /* 336 x 280 rectangle */
  .rectangle{left:337px;top:309px;width:336px;height:278px}
  .rectangle .headline{left:17px;top:10px;font-size:25px}
  .rectangle .features{left:15px;top:57px;font-size:13px;line-height:17px}
  .rectangle .features li{padding-left:19px;margin-bottom:8px}
  .rectangle .photo{left:183px;top:49px;width:135px;height:160px}
  .rectangle .footer{position:absolute;left:0;top:208px;width:336px;height:70px;background:linear-gradient(var(--white),var(--paper));border-top:3px solid var(--green)}
  .rectangle .footer .divider{position:absolute;left:0;top:0}
  .rectangle .brand{left:8px;top:11px;gap:8px}
  .rectangle .brand-dot{width:46px;height:46px}
  .rectangle .brand-name{font-size:31px}
  .rectangle .cta{left:202px;top:20px;width:113px;height:34px;font-size:19px}
</style>
</head>
<body>
<svg width="0" height="0" style="position:absolute">
  <defs>
    <symbol id="tick" viewBox="0 0 12 10"><path d="M1 5.2 L4.4 8.6 L11 1.4" fill="none" stroke="#84c12e" stroke-width="2.2" stroke-linecap="round" stroke-linejoin="round"/></symbol>
  </defs>
</svg>

<main class="stage">

  <section class="banner skyscraper" aria-label="160 by 600 banner">
    <svg class="top" width="159" height="160" viewBox="0 0 159 160">
      <polygon points="0,0 159,0 159,118 0,150" fill="#ffffff"/>
      <polygon points="0,150 159,118 159,124 0,156" fill="#84c12e"/>
    </svg>
    <div class="brand">
      <span class="brand-dot"></span>
      <span class="brand-name">velHelm</span>
    </div>
    <h2 class="headline">Innovative<br>Web<br>Solutions</h2>
    <ul class="features">
      <li><svg><use href="#tick"/></svg>Pay Per Performance<br>SEO service</li>
      <li><svg><use href="#tick"/></svg>Guaranteed Zumbly<br>page 1 ranking</li>
      <li><svg><use href="#tick"/></svg>Only $197 per month<br>(+ performance<br>bonus)</li>
    </ul>
    <div class="photo" role="img" aria-label="Photo of a smiling businesswoman pointing towards the text"></div>
    <div class="footer"><span class="cta">Learn More</span></div>
  </section>

  <section class="banner leaderboard" aria-label="728 by 90 banner">
    <svg class="top" width="200" height="90" viewBox="0 0 200 90">
      <polygon points="0,0 190,0 150,90 0,90" fill="#ffffff"/>
      <polygon points="190,0 197,0 157,90 150,90" fill="#84c12e"/>
    </svg>
    <div class="brand">
      <span class="brand-dot"></span>
      <span class="brand-name">velHelm</span>
    </div>
    <h2 class="headline">Innovative Web Solutions</h2>
    <ul class="features col-a">
      <li><svg><use href="#tick"/></svg>Pay Per Performance SEO service</li>
      <li><svg><use href="#tick"/></svg>Guaranteed Zumbly page 1 ranking</li>
    </ul>
    <ul class="features col-b">
      <li><svg><use href="#tick"/></svg>Only $197 per month<br>(+performance bonus)</li>
    </ul>
    <div class="photo" role="img" aria-label="Photo of a smiling businesswoman pointing towards the text"></div>
    <span class="cta">Learn More</span>
  </section>

  <section class="banner rectangle" aria-label="336 by 280 banner">
    <h2 class="headline">Innovative Web Solutions</h2>
    <ul class="features">
      <li><svg><use href="#tick"/></svg>Pay Per Performance<br>SEO service</li>
      <li><svg><use href="#tick"/></svg>Guaranteed Zumbly<br>page 1 ranking</li>
      <li><svg><use href="#tick"/></svg>Only $197 per month<br>(+ performance<br>bonus)</li>
    </ul>
    <div class="photo" role="img" aria-label="Photo of a smiling businesswoman pointing towards the text"></div>
    <div class="footer">
      <svg class="divider" width="336" height="67" viewBox="0 0 336 67">
        <line x1="186" y1="0" x2="170" y2="67" stroke="#d2d2d2" stroke-width="1.5"/>
      </svg>
      <div class="brand">
        <span class="brand-dot"></span>
        <span class="brand-name">velHelm</span>
      </div>
      <span class="cta">Learn More</span>
    </div>
  </section>

</main>
</body>
</html>
```